High End Business Card Design for Flooring Store

Looking for a new card design for our hardwood flooring company. We have no print budget for these and are open to cards made from wood, metal, cardstock with embossed print ... or any combination of these. No plastic.

We sell luxury products and I want the cards to reflect our image of quality and class.

Our contact information as such;
Employee Name
418 Colbrook Blvd.
Harwick, ON
K9R-3M5
(555) 214-3968
Employee email @velkaflooring.com

Target Market(s)

Home Builders

Contact Information for Business Card

Emnployee name, business contact information

```html
<!DOCTYPE html>
<html lang="en">
<head>
<meta charset="utf-8">
<title>Velka Flooring &amp; Stairs – Business Card</title>
<link href="https://fonts.googleapis.com/css2?family=Montserrat:wght@400;500;700&display=swap" rel="stylesheet">
<style>
  :root {
    --backdrop: #aaaaaa;
    --front-light: #f7f7f7;
    --front-grain: #dcdcdc;
    --back-light: #7a5640;
    --back-dark: #5a3b28;
    --brand-red: #8e1f1a;
    --brand-gold: #e4b021;
    --tag-grey: #4a4a4a;
    --ink-white: #ffffff;
  }
  * { margin: 0; padding: 0; box-sizing: border-box; }
  html, body {
    width: 1200px; height: 1000px; overflow: hidden;
    background: var(--backdrop);
    font-family: "Montserrat", sans-serif;
  }
  .canvas { position: relative; width: 1200px; height: 1000px; }

  .card {
    position: absolute; left: 293px; width: 615px; height: 354px;
    border-radius: 16px; overflow: hidden;
    box-shadow: 0 8px 18px rgba(0,0,0,0.28);
  }
  .card-front { top: 130px; }
  .card-back { top: 551px; }

  .card-surface { position: absolute; inset: 0; }
  .card-front .card-surface {
    background: linear-gradient(180deg, var(--front-light) 0%, var(--front-grain) 50%, var(--front-light) 100%);
  }
  .card-back .card-surface {
    background: linear-gradient(180deg, var(--back-dark) 0%, var(--back-light) 45%, var(--back-dark) 100%);
  }

  /* front */
  .front-mark { position: absolute; left: 96px; top: 120px; width: 55px; height: 85px; background: var(--brand-gold); }
  .front-name {
    position: absolute; left: 154px; top: 105px;
    font-size: 104px; font-weight: 500; line-height: 1; color: var(--brand-red);
  }
  .front-tagline {
    position: absolute; left: 0; width: 640px; top: 210px; text-align: center;
    font-size: 22px; line-height: 27px; color: var(--tag-grey);
  }

  /* back */
  .back-brand { position: absolute; left: 37px; top: 142px; width: 276px; color: var(--ink-white); }
  .back-mark { position: absolute; left: 0; top: 4px; width: 36px; height: 50px; background: var(--ink-white); }
  .back-name { position: absolute; left: 40px; top: 0; font-size: 58px; font-weight: 500; line-height: 1; }
  .back-tagline {
    position: absolute; left: 0; width: 276px; top: 58px; text-align: center;
    font-size: 14px; line-height: 16px;
  }
  .back-divider { position: absolute; left: 320px; top: 122px; width: 2px; height: 130px; background: var(--ink-white); }
  .contact {
    position: absolute; left: 345px; width: 220px; top: 140px; text-align: center; color: var(--ink-white);
  }
  .contact-name { font-size: 17px; font-weight: 700; line-height: 22px; }
  .contact-icons { display: flex; justify-content: center; gap: 5px; margin-top: 9px; height: 19px; }
  .contact-icons svg { width: 19px; height: 19px; display: block; }
  .contact-line { font-size: 15px; line-height: 17px; }
  .contact-phone { margin-top: 8px; }
  .address {
    position: absolute; left: 0; width: 615px; top: 317px; text-align: center;
    font-size: 13px; color: var(--ink-white);
  }
</style>
</head>
<body>
<div class="canvas">

  <section class="card card-front">
    <div class="card-surface" role="img" aria-label="Whitewashed light wood grain surface"></div>
    <div class="front-mark"></div>
    <div class="front-name">Velka</div>
    <div class="front-tagline">Planchers &amp; Escaliers<br>Flooring &amp; Stairs</div>
  </section>

  <section class="card card-back">
    <div class="card-surface" role="img" aria-label="Dark walnut wood grain surface"></div>
    <div class="back-brand">
      <div class="back-mark"></div>
      <div class="back-name">Velka</div>
      <div class="back-tagline">Planchers &amp; Escaliers<br>Flooring &amp; Stairs</div>
    </div>
    <div class="back-divider"></div>
    <div class="contact">
      <div class="contact-name">Employee Name</div>
      <div class="contact-icons">
        <svg viewBox="0 0 20 20" aria-label="Phone">
          <circle cx="10" cy="10" r="10" fill="#ffffff"/>
          <path d="M7 5.2c.5-.3 1-.2 1.3.3l.9 1.6c.2.4.1.9-.3 1.2l-.6.4c.5 1.1 1.3 1.9 2.4 2.4l.4-.6c.3-.4.8-.5 1.2-.3l1.6.9c.5.3.6.8.3 1.3l-.6.9c-.4.6-1.2.8-1.9.5C9.6 12.8 7.2 10.4 6.1 8.3c-.3-.7-.1-1.5.5-1.9z" fill="#5a3b28"/>
        </svg>
        <svg viewBox="0 0 20 20" aria-label="Email">
          <circle cx="10" cy="10" r="10" fill="#ffffff"/>
          <rect x="5" y="6.5" width="10" height="7" rx="1" fill="#5a3b28"/>
          <path d="M5.5 7.2 10 10.6 14.5 7.2" fill="none" stroke="#ffffff" stroke-width="0.9"/>
        </svg>
      </div>
      <div class="contact-line contact-phone">(555) 214-3968</div>
      <div class="contact-line">email @velkaflooring.com</div>
    </div>
    <div class="address">418 Colbrook Blvd. Harwick, ON K9R-3M5</div>
  </section>

</div>
</body>
</html>
```